Purely Brindlewick Soap business needs a soap box design

Update 10/3/16 The soap box that I will be using is attached and would like the open circle in the upper right hand corner and vertical
Have attached a suggestion for a style, but open to all designs
My soaps will be more for the mid to high end consumer that wants a natural soap
Would love a box that may be used as a universal soap box

Target Market(s)

high end clients

Industry/Entity Type

Business

Colors
abd036
1b1b1b

Requirements
Must have
• The colors in my logo....green,white and black
• Update 10/3/16 The soap box that I will be using is attached and would like the open circle in the upper right hand corner and the soap box to be horizontal.
Nice to have
• I would like a design that would allow me to add a scent label so I can use a single design box, but not mandatory.
• Keeping with the name "Purely Brindlewick Soap" I would like a simple, but elegant soap box.

```html
<!DOCTYPE html>
<html lang="en">
<head>
<meta charset="utf-8">
<title>Purely Brindlewick Soap – Box Dieline</title>
<link rel="stylesheet" href="https://fonts.googleapis.com/css2?family=Great+Vibes&family=Cormorant+Garamond:wght@500&display=swap">
<style>
  :root {
    --paper: #ffffff;
    --sage: #8a9c62;
    --sage-mark: #7f9556;
    --ink: #111111;
    --cut-line: #1fa86a;
    --fold-line: #2b2b2b;
    --bleed-line: #e0707a;
    --dimension: #2a8bd0;
  }
  html, body {
    margin: 0;
    padding: 0;
    width: 1200px;
    height: 900px;
    overflow: hidden;
    background: var(--paper);
  }
  .dieline {
    display: block;
    width: 1200px;
    height: 900px;
  }
  .cut-outline { fill: none; stroke: var(--cut-line); stroke-width: 1.2; }
  .panel-sage { fill: var(--sage); }
  .panel-black { fill: var(--ink); }
  .label-area { fill: var(--paper); }
  .label-edge { stroke: var(--bleed-line); stroke-width: 0.8; stroke-dasharray: 2 2; }
  .fold { stroke: var(--fold-line); stroke-width: 0.9; }
  .brand-dot { fill: var(--sage-mark); }
  .brand-name {
    font-family: "Great Vibes", cursive;
    font-size: 54px;
    fill: var(--ink);
  }
  .brand-tagline {
    font-family: "Cormorant Garamond", serif;
    font-weight: 500;
    font-size: 17px;
    letter-spacing: 4.4px;
    fill: var(--ink);
  }
  .dimension-line { stroke: var(--dimension); stroke-width: 1; }
  .dimension-head, .label-marker { fill: var(--dimension); }
  .dimension-text {
    font-family: Arial, Helvetica, sans-serif;
    font-size: 11px;
    fill: var(--dimension);
  }
</style>
</head>
<body>
<svg class="dieline" viewBox="0 0 1024 768" xmlns="http://www.w3.org/2000/svg" aria-label="Purely Brindlewick Soap box dieline">
  <!-- cut outline -->
  <path class="cut-outline" d="M143 104 H232 V40 Q232 10 262 10 H468 Q497 10 497 40 V104 H583 L600 200 H835 L893 215 V565 L835 582 H600 L583 680 H497 V730 Q497 760 468 760 H262 Q232 760 232 730 V680 H143 L120 580 V215 Z"/>

  <!-- end tuck flaps -->
  <path class="panel-black" d="M244 104 V40 Q244 22 262 22 H472 Q490 22 490 40 V104 Z"/>
  <path class="panel-black" d="M244 672 V734 Q244 752 262 752 H472 Q490 752 486 734 V672 Z"/>

  <!-- left dust flap -->
  <polygon class="panel-sage" points="150,122 244,122 244,655 150,655 132,560 132,215"/>
  <!-- front panel -->
  <rect class="panel-sage" x="244" y="104" width="238" height="568"/>
  <!-- right dust flap -->
  <polygon class="panel-sage" points="482,122 572,122 595,215 595,560 572,655 482,655"/>
  <!-- side panel -->
  <rect class="panel-sage" x="595" y="218" width="237" height="340"/>
  <!-- glue tab -->
  <polygon class="panel-black" points="832,218 882,228 882,548 832,558"/>

  <!-- fold lines -->
  <line class="fold" x1="244" y1="104" x2="244" y2="222"/>
  <line class="fold" x1="244" y1="553" x2="244" y2="672"/>
  <line class="fold" x1="482" y1="104" x2="482" y2="222"/>
  <line class="fold" x1="482" y1="553" x2="482" y2="672"/>
  <line class="fold" x1="595" y1="218" x2="595" y2="558"/>

  <!-- scent label area -->
  <rect class="label-area" x="246" y="220" width="234" height="335"/>
  <line class="label-edge" x1="246" y1="220" x2="246" y2="555"/>
  <line class="label-edge" x1="480" y1="220" x2="480" y2="555"/>
  <polygon class="label-marker" points="249,385 253,382 253,388"/>
  <polygon class="label-marker" points="477,385 473,382 473,388"/>

  <!-- brand lockup -->
  <g class="brand">
    <circle class="brand-dot" cx="310" cy="388" r="30"/>
    <text class="brand-name" transform="translate(414 540) rotate(-90)">Purely Brindlewick</text>
    <text class="brand-tagline" transform="translate(450 482) rotate(-90)">handcrafted soap</text>
  </g>

  <!-- flap depth dimension -->
  <g class="dimension">
    <line class="dimension-line" x1="203" y1="126" x2="203" y2="214"/>
    <polygon class="dimension-head" points="203,122 199,130 207,130"/>
    <polygon class="dimension-head" points="203,218 199,210 207,210"/>
    <rect x="185" y="163" width="38" height="14" fill="var(--sage)"/>
    <text class="dimension-text" x="187" y="174">0.936</text>
  </g>
</svg>
</body>
</html>
```